High Profile Government Site Design

We need some concept designs for a website that will be used for reporting campaign contributions to politicians. I am including some images to give you an idea of what has been done so far. Basically the deliverable should be a landing page and perhaps a content page we can use to put in our charts and data tables. The landing page should be in a tiled format so we can list featured elections, show some general inforgraphical information, and offer a search capability. We do not want you to use the existing site design or logo in the images provided but to come up with your own concepts so we can share them with the committee that decides the final look. There is an existing site for this application located at http://apps.velmorstate.gov/apps/election/cfs/search/CandidateSearch.aspx . If you win there may be more work on this project and other projects.

Target Market(s)

Political

Industry/Entity Type

Government

Number of Pages Required

2 page

Font styles to use
Sans Serif

Colors

Designer to choose colors to be used in the design.

Requirements
Nice to have
• Some ideas are on the landing page offering up some segments for races of interest, contributors of interest, some statistical information, and potentially a search bar.
Should not have
• Should not use the current design or logo

```html
<!DOCTYPE html>
<html lang="en">
<head>
<meta charset="utf-8">
<title>Civic Ledger</title>
<link rel="stylesheet" href="https://fonts.googleapis.com/css2?family=Montserrat:wght@400;500;600;700&display=swap">
<style>
  :root {
    --bg-top: #2a1478;
    --bg-mid: #1a0c58;
    --bg-bottom: #0b0630;
    --white: #ffffff;
    --nav-dark: #000000;
    --nav-active: #ff6c00;
    --tile-green: #27ae60;
    --tile-orange: #e67e22;
    --tile-red: #e74c3c;
    --tile-purple: #8e44ad;
    --tile-slate: #34495e;
    --tile-blue: #3498db;
    --tile-gray: #95a5a6;
    --divider: rgba(255,255,255,0.25);
    --footer-text: #c9c4e0;
  }
  * { box-sizing: border-box; margin: 0; padding: 0; }
  html, body { width: 1200px; height: 738px; overflow: hidden; }
  body {
    font-family: "Montserrat", Arial, sans-serif;
    color: var(--white);
    background:
      radial-gradient(ellipse at 75% 10%, rgba(90,50,200,0.55), transparent 55%),
      linear-gradient(160deg, var(--bg-top) 0%, var(--bg-mid) 45%, var(--bg-bottom) 100%);
    position: relative;
  }
  a { color: inherit; text-decoration: none; }
  .page { position: absolute; left: 75px; top: 0; width: 1051px; }

  .site-header { height: 88px; display: flex; align-items: center; justify-content: space-between; }
  .site-title { font-size: 29px; font-weight: 700; letter-spacing: 0.2px; margin-top: -6px; }
  .social-links { display: flex; gap: 19px; margin-top: -6px; }
  .social-links span { width: 18px; height: 18px; border-radius: 50%; background: var(--white); display: block; }

  .main-nav { height: 44px; display: flex; align-items: center; }
  .nav-item {
    height: 44px; display: flex; align-items: center; justify-content: center;
    background: var(--nav-dark); font-size: 12.5px; font-weight: 700; margin-right: 9px;
  }
  .nav-item.active { background: var(--nav-active); }
  .search-box {
    margin-left: auto; width: 269px; height: 44px; border: 1px solid rgba(255,255,255,0.6);
    display: flex; align-items: center; justify-content: space-between; padding: 0 14px 0 16px;
    font-size: 13px; font-weight: 500;
  }

  .tiles {
    margin-top: 16px;
    display: grid;
    grid-template-columns: 346px 213px 213px 242px;
    grid-template-rows: 182px 341px;
    column-gap: 12px; row-gap: 13px;
  }
  .tile { position: relative; overflow: hidden; }
  .tile-photo { background: linear-gradient(135deg, #7a6a66 0%, #c9c3c0 40%, #a8322b 80%, #6e1f1a 100%); }
  .tile-link { padding: 20px; display: flex; flex-direction: column; justify-content: space-between; }
  .tile-link .tile-label { font-size: 16px; font-weight: 700; letter-spacing: 0.3px; margin-bottom: -2px; }
  .tile-about { background: var(--tile-green); }
  .tile-services { background: var(--tile-orange); padding-left: 24px; }
  .tile-blog { background: var(--tile-red); }

  .panel-title { font-size: 16.5px; font-weight: 700; letter-spacing: 0.3px; }
  .featured { background: var(--tile-purple); padding: 22px 20px 0 17px; }
  .election-list { list-style: none; margin-top: 14px; }
  .election-list li {
    height: 39px; display: flex; align-items: center; gap: 17px;
    font-size: 12.5px; border-bottom: 1px solid var(--divider); width: 310px; white-space: nowrap;
  }
  .election-list li svg { flex-shrink: 0; }
  .election-list li:last-child { border-bottom: none; }

  .general { grid-column: 2 / span 2; background: var(--tile-slate); padding: 22px 22px; }
  .infographic {
    position: absolute; left: 78px; top: 54px; width: 282px; height: 268px;
    background: linear-gradient(180deg, #e8584a 0%, #e74c3c 60%, #1f5f86 100%);
    border-radius: 4px;
  }

  .side-stack { display: flex; flex-direction: column; gap: 10px; }
  .news { background: var(--tile-blue); height: 166px; padding: 22px 20px; }
  .news-head { display: flex; justify-content: space-between; align-items: center; }
  .news-date { font-size: 13.5px; font-weight: 700; margin-top: 16px; }
  .news-text { font-size: 13px; line-height: 20px; margin-top: 6px; }
  .read-more { font-size: 11px; font-weight: 700; margin-top: 10px; display: block; }

  .contact { background: var(--tile-gray); height: 165px; padding: 18px 20px; }
  .contact-name { font-size: 13.5px; font-weight: 700; margin-top: 10px; }
  .contact-line { font-size: 13px; line-height: 20px; margin-top: 4px; }
  .contact-row { display: flex; align-items: center; gap: 22px; font-size: 13px; margin-top: 6px; }
  .contact-row svg { flex-shrink: 0; }

  .site-footer { position: absolute; top: 704px; left: 0; width: 1200px; text-align: center; font-size: 11.5px; color: var(--footer-text); }
</style>
</head>
<body>
<div class="page">
  <header class="site-header">
    <div class="site-title">CIVIC LEDGER</div>
    <nav class="social-links" aria-label="Social profiles">
      <span></span><span></span><span></span><span></span><span></span><span></span>
    </nav>
  </header>

  <nav class="main-nav">
    <a class="nav-item active" style="width:89px">HOME</a>
    <a class="nav-item" style="width:89px">ABOUT</a>
    <a class="nav-item" style="width:177px">FEATURED ELECTIONS</a>
    <a class="nav-item" style="width:89px">BLOG</a>
    <a class="nav-item" style="width:144px">NEWS &amp; EVENTS</a>
    <a class="nav-item" style="width:89px">CONTACT</a>
    <div class="search-box">
      <span>Search...</span>
      <svg width="13" height="13" viewBox="0 0 14 14"><circle cx="5.5" cy="5.5" r="4.3" fill="none" stroke="#fff" stroke-width="2"/><line x1="8.8" y1="8.8" x2="13" y2="13" stroke="#fff" stroke-width="2.2" stroke-linecap="round"/></svg>
    </div>
  </nav>

  <main class="tiles">
    <div class="tile tile-photo" role="img" aria-label="Photo of ballot papers being counted in trays on a table"></div>

    <a class="tile tile-link tile-about">
      <svg width="84" height="80" viewBox="0 0 84 80" fill="#fff">
        <circle cx="14" cy="14" r="12"/><circle cx="70" cy="14" r="12"/>
        <path d="M0 58 a14 14 0 0 1 14 -26 h6 a20 20 0 0 0 0 26z"/>
        <path d="M84 58 a14 14 0 0 0 -14 -26 h-6 a20 20 0 0 1 0 26z"/>
        <circle cx="42" cy="26" r="17" stroke="#27ae60" stroke-width="3"/>
        <path d="M16 80 v-12 a18 18 0 0 1 18 -18 h16 a18 18 0 0 1 18 18 v12z" stroke="#27ae60" stroke-width="3"/>
      </svg>
      <span class="tile-label">ABOUT US</span>
    </a>

    <a class="tile tile-link tile-services">
      <svg width="86" height="74" viewBox="0 0 86 74" fill="#fff">
        <path d="M28 12 v-6 a6 6 0 0 1 6 -6 h18 a6 6 0 0 1 6 6 v6 h-6 v-5 h-18 v5z"/>
        <rect x="0" y="14" width="13" height="60" rx="5"/>
        <rect x="18" y="14" width="50" height="60"/>
        <rect x="73" y="14" width="13" height="60" rx="5"/>
      </svg>
      <span class="tile-label">SERVICES</span>
    </a>

    <a class="tile tile-link tile-blog">
      <svg width="76" height="76" viewBox="0 0 76 76" fill="#fff">
        <circle cx="10" cy="66" r="10"/>
        <path d="M0 28 a48 48 0 0 1 48 48 h-12 a36 36 0 0 0 -36 -36z"/>
        <path d="M0 0 a76 76 0 0 1 76 76 h-12 a64 64 0 0 0 -64 -64z"/>
      </svg>
      <span class="tile-label">RECENT BLOG POST</span>
    </a>

    <section class="tile featured">
      <h2 class="panel-title">FEATURED ELECTIONS</h2>
      <ul class="election-list">
        <li><svg width="14" height="11" viewBox="0 0 14 11"><path d="M1 5.5 l4 4 l8 -8" fill="none" stroke="#fff" stroke-width="2.6"/></svg>2016 Election Night Results</li>
        <li><svg width="14" height="11" viewBox="0 0 14 11"><path d="M1 5.5 l4 4 l8 -8" fill="none" stroke="#fff" stroke-width="2.6"/></svg>Elections Calendar &amp; Upcoming Events</li>
        <li><svg width="14" height="11" viewBox="0 0 14 11"><path d="M1 5.5 l4 4 l8 -8" fill="none" stroke="#fff" stroke-width="2.6"/></svg>Voting In This Election</li>
        <li><svg width="14" height="11" viewBox="0 0 14 11"><path d="M1 5.5 l4 4 l8 -8" fill="none" stroke="#fff" stroke-width="2.6"/></svg>Campaign Finance &amp; Reporting</li>
        <li><svg width="14" height="11" viewBox="0 0 14 11"><path d="M1 5.5 l4 4 l8 -8" fill="none" stroke="#fff" stroke-width="2.6"/></svg>Running for Office</li>
        <li><svg width="14" height="11" viewBox="0 0 14 11"><path d="M1 5.5 l4 4 l8 -8" fill="none" stroke="#fff" stroke-width="2.6"/></svg>Voter Registration &amp; Historical Election Data</li>
        <li><svg width="14" height="11" viewBox="0 0 14 11"><path d="M1 5.5 l4 4 l8 -8" fill="none" stroke="#fff" stroke-width="2.6"/></svg>Velmor Election Laws &amp; Publications</li>
      </ul>
    </section>

    <section class="tile general">
      <h2 class="panel-title">GENERAL INFORMATION</h2>
      <div class="infographic" role="img" aria-label="Election day infographic illustration with candidates, a calendar, a line chart and a magnifying glass"></div>
    </section>

    <div class="side-stack">
      <section class="news">
        <div class="news-head">
          <h2 class="panel-title">NEWS &amp; EVENTS</h2>
          <svg width="30" height="14" viewBox="0 0 30 14"><path d="M6 1 l-5 6 l5 6 M24 1 l5 6 l-5 6" fill="none" stroke="#fff" stroke-width="2"/></svg>
        </div>
        <p class="news-date">MAY 16, 2017</p>
        <p class="news-text">Nemo enim ipsam voluptatem voluptas sit aspernatur..</p>
        <a class="read-more">Read More</a>
      </section>
      <section class="contact">
        <h2 class="panel-title">CONTACT US</h2>
        <p class="contact-name">CIVIC LEDGER</p>
        <p class="contact-line">4120 Linden Row<br>Velmor City, VC 20418</p>
        <div class="contact-row">
          <svg width="12" height="12" viewBox="0 0 12 12"><path d="M2 0 h2 l1 3 l-1.5 1.5 a7 7 0 0 0 4 4 l1.5 -1.5 l3 1 v2 a2 2 0 0 1 -2 2 a10 10 0 0 1 -10 -10 a2 2 0 0 1 2 -2z" fill="#fff"/></svg>
          <span>1-800-555-0148</span>
        </div>
        <div class="contact-row">
          <svg width="13" height="10" viewBox="0 0 13 10"><rect width="13" height="10" rx="1" fill="#fff"/><path d="M0.5 1 l6 4.5 l6 -4.5" fill="none" stroke="#95a5a6" stroke-width="1.2"/></svg>
          <span>Email</span>
        </div>
      </section>
    </div>
  </main>
</div>
<footer class="site-footer">Copyright © 2017. Company Name. All Right Reserved</footer>
</body>
</html>
```